Visitenkarten-Design für Familienunternehmen (Apotheke)
Zielgruppe
Wir sind ein Familienunternehmen und betreiben 4 Apotheken (alle eigene Namen: Lindenhain-Apotheke; Quellen-Apotheke; Apotheke Am Brunnentor und Vitalora-Apotheke)
Wir beginnen, diese alle unter Eulen-Apotheken zusammenzufassen. www.eulen-apotheken.de (die Vitalora-Apotheke eröffnet erst am 1.1.18 neu, daher noch nicht online)
Konkret möchten wir für die Mitarbeiter der Vitalora-Apotheke Visitenkarten mit Porträt für Kunden erstellen.
Aktuell sind wir ca. 10 Mitarbeiter in dieser Apotheke. Ggf. möchten wir mittelfristig alle Mitarbeiter aller Apotheken (ca. 50-60) mit Visitenkarten ausstatten.
Aufgabenstellung
Wir haben vor Jahren selbst laienhaft eine Visitenkarte erstellt
Ich habe gegoogelt und andere Beispiele mit Porträt gefunden.
Wir suchen eine Visitenkarte, die sowohl das Logo Vitalora-Apotheke inkl. Adresse, Telefonnummer etc. hat (kann auch optisch verschoben werden - oben Logo - unten Adresse o.ä) , den Namen des Mitarbeitern und Beruf (Apothekerin o.ä.) und 2-3 Schlagwörter/Schlagsätze zu der Qualifikation des Mitarbeiters.
(die Vitalora-Apotheke hat eine Spezialzertifizierung 'Wiegensichere Offizin' und darf daher auch das Logo Wiegensichere Offizin nutzen. Eventuell gibt es die Möglichkeit dieses auch - nicht konkurrierend - neben dem Hauptlogo Vitalora-Apotheke unterzubringen)
unten gerne 'Eulen-Apotheken' o.ä. als Dachmarke
Mutter-Kind-Expertin (Zertifizierung Wiegensichere Offizin)
Fachberaterin für Darmgesundheit
!! Seriös, weniger verspielt. Druckbar für Druckwerkel, wir nehmen gerne Tipps zu Papier und Stärke an!
Ziel: Klares Design, wo einfach der Kopf des Mitarbeiters gewechselt werden kann und die Qualifikation, um für alle Mitarbeiter gleiche CI zu erstellen

```html
<!DOCTYPE html>
<html lang="de">
<head>
<meta charset="utf-8">
<title>Visitenkarte Vitalora-Apotheke</title>
<link href="https://fonts.googleapis.com/css2?family=Arimo:wght@400;700&display=swap" rel="stylesheet">
<style>
  :root {
    --stage: #d9333a;
    --card: #f7f7f7;
    --red: #d8262e;
    --ink: #2f2f31;
    --grey: #555558;
    --seal-fill: #e4e4e6;
    --photo-top: #eceae8;
    --photo-bottom: #b9a595;
  }
  * { margin: 0; padding: 0; box-sizing: border-box; }
  html, body { width: 1200px; height: 756px; overflow: hidden; }
  body {
    background: var(--stage);
    font-family: "Arimo", Arial, sans-serif;
    position: relative;
  }
  .card {
    position: absolute;
    left: 302px;
    width: 595px;
    height: 330px;
    background: var(--card);
    overflow: hidden;
  }
  .card--front { top: 33px; }
  .card--back { top: 393px; }

  .brand {
    position: absolute;
    font-weight: 700;
    color: var(--ink);
    line-height: 0.95;
    letter-spacing: -0.5px;
  }
  .card--front .brand { right: 30px; top: 40px; font-size: 25px; text-align: right; }

  .portrait {
    position: absolute;
    left: 0; top: 100px;
    width: 212px; height: 218px;
    background: linear-gradient(180deg, var(--photo-top) 0%, var(--photo-bottom) 100%);
  }
  .divider { position: absolute; background: var(--ink); }
  .card--front .divider { left: 220px; top: 98px; width: 5px; height: 153px; }

  .person { position: absolute; left: 244px; top: 122px; color: var(--red); }
  .person__name { font-size: 20px; line-height: 24px; }
  .person__role { font-size: 17px; line-height: 22px; margin-top: 5px; margin-left: 2px; }
  .person__skills { font-size: 17px; line-height: 21px; margin-top: 22px; }

  .base-band { position: absolute; left: 0; bottom: 0; width: 595px; height: 12px; }

  /* back */
  .seal {
    position: absolute; left: 76px; top: 58px;
    width: 100px; height: 100px;
    background: var(--seal-fill);
  }
  .card--back .brand { left: 0; width: 252px; top: 184px; font-size: 32px; text-align: center; }
  .card--back .divider { left: 253px; top: 98px; width: 3px; height: 152px; }

  .qualifications {
    position: absolute; left: 281px; top: 88px;
    color: var(--red); font-size: 14px; line-height: 17px;
  }
  .contact { position: absolute; left: 288px; top: 0; list-style: none; color: var(--grey); font-size: 13px; line-height: 16px; }
  .contact li { position: absolute; left: 0; white-space: nowrap; }
  .contact svg { position: absolute; left: 0; top: 0; }
  .contact span { position: absolute; left: 26px; top: 0; }
  .contact .address { top: 156px; }
  .contact .phone { top: 196px; }
  .contact .mail { top: 220px; }
  .contact .web { top: 241px; }
</style>
</head>
<body>

<section class="card card--front">
  <div class="brand">Vitalora-<br>Apotheke</div>

  <div class="portrait" role="img" aria-label="Porträtfoto der Mitarbeiterin"></div>
  <div class="divider"></div>

  <div class="person">
    <p class="person__name">Johanna Berktold</p>
    <p class="person__role">Apothekerin</p>
    <p class="person__skills">Mutter-Kind-Expertin<br>Fachberaterin für Darmgesundheit</p>
  </div>

  <svg class="base-band" viewBox="0 0 595 12" aria-hidden="true">
    <rect x="260" y="2" width="335" height="10" fill="#d8262e"/>
    <polygon points="0,0 292,0 272,12 0,12" fill="#2f2f31"/>
  </svg>
</section>

<section class="card card--back">
  <div class="seal" role="img" aria-label="Zertifikatssiegel Wiegensichere Offizin"></div>

  <div class="brand">Vitalora-<br>Apotheke</div>

  <div class="divider"></div>

  <p class="qualifications">Mutter-Kind-Expertin<br>(Zertifizierung Wiegensichere Offizin)<br>Fachberaterin für Darmgesundheit</p>

  <ul class="contact">
    <li class="address">
      <svg width="12" height="16" viewBox="0 0 12 16" aria-hidden="true"><path d="M6 0C2.7 0 0 2.6 0 5.9 0 10 6 16 6 16s6-6 6-10.1C12 2.6 9.3 0 6 0zm0 8.2A2.3 2.3 0 1 1 6 3.6a2.3 2.3 0 0 1 0 4.6z" fill="#d8262e"/></svg>
      <span>Kesselweg<br>15&nbsp;&nbsp;93410 Talbrunn</span>
    </li>
    <li class="phone">
      <svg width="12" height="18" viewBox="0 0 12 18" aria-hidden="true"><rect x="1" y="1" width="10" height="16" rx="2" fill="none" stroke="#d8262e" stroke-width="1.6"/><circle cx="6" cy="14.2" r="1" fill="#d8262e"/></svg>
      <span>0961 / 448210 - 448210-1</span>
    </li>
    <li class="mail">
      <svg width="16" height="12" viewBox="0 0 16 12" aria-hidden="true"><rect x="0" y="1" width="16" height="10" fill="#d8262e"/><path d="M0 1l8 6 8-6" fill="none" stroke="#f7f7f7" stroke-width="1.2"/></svg>
      <span>vitalora@eulen-apotheken.de</span>
    </li>
    <li class="web">
      <svg width="15" height="15" viewBox="0 0 16 16" aria-hidden="true"><g fill="none" stroke="#d8262e" stroke-width="1.2"><circle cx="8" cy="8" r="7"/><ellipse cx="8" cy="8" rx="3" ry="7"/><path d="M1 8h14M2.5 4.5h11M2.5 11.5h11"/></g></svg>
      <span>www.eulen-apotheken.de</span>
    </li>
  </ul>
</section>

</body>
</html>
```